A land page lead collector for people who want to reduce there postage costs

We are looking to create a single page website landing page to collect leads of people who want to reduce there postage costs.

The form should basically ask:

Name:
Business Name:
Address:
Town:
Post Code:
Email:
Phone:
Letter Volume Per Week:
Parcel Volume Per Week:

We should basically be advertising cheaper postage costs.

We will not be showing prices on this website we will just be collecting the leads.

Our competition website is as follows https://mailfernquest.com

But we are not a online service. This is just a collector to get leads of people who want to save money on there postage costs.
Updates

Target Market(s)

Small and medium sized enterprises

Industry/Entity Type

Advertising

Number of Pages Required

1 page

Colors
ec2027
0356a4

Requirements
Must have
• Form above the fold of the page
Nice to have
• Colour red and blue.
• Parallax design would be nice.

```html
<!DOCTYPE html>
<html lang="en">
<head>
<meta charset="utf-8">
<title>Reduce Your Postage Costs</title>
<link rel="stylesheet" href="https://fonts.googleapis.com/css2?family=Questrial&family=Oswald:wght@500&family=Noto+Sans:wght@400&family=Lato:wght@400&display=swap">
<style>
  :root {
    --red: #ec2027;
    --blue: #0356a4;
    --white: #ffffff;
    --field: #ececec;
    --field-border: #dcdcdc;
    --field-text: #8a8a8a;
    --ink: #222222;
  }
  * { box-sizing: border-box; margin: 0; padding: 0; }
  html, body { width: 934px; height: 1200px; overflow: hidden; }
  body { position: relative; background: var(--red); font-family: "Noto Sans", sans-serif; }

  .page-header { position: absolute; left: 0; top: 0; width: 934px; height: 150px; background: var(--red); }
  .headline { position: absolute; left: 130px; top: 38px; color: var(--white); font-family: "Questrial", sans-serif; font-weight: 400; text-transform: uppercase; line-height: 1; }
  .headline .lead { display: block; font-size: 25px; }
  .headline .main { display: block; font-size: 33px; margin-top: 3px; }

  .hero { position: absolute; left: 0; top: 118px; width: 934px; height: 554px;
    background: linear-gradient(135deg, #9c8462 0%, #b9a27c 35%, #8d7656 65%, #a58d68 100%); }
  .hero-postbox { position: absolute; left: 560px; top: 226px; width: 160px; height: 378px;
    background: linear-gradient(180deg, #d8261f, #b81d18); border-radius: 3px; }
  .hero-edge { position: absolute; left: 0; top: 110px; }

  .lead-form { position: absolute; left: 129px; top: 230px; width: 349px; height: 352px; background: var(--white); border-radius: 4px; }
  .field { position: absolute; height: 32px; background: var(--field); border: 1px solid var(--field-border); border-radius: 2px;
    font-family: "Noto Sans", sans-serif; font-size: 12px; color: var(--field-text); padding: 0 8px; line-height: 30px; }
  .field.half { width: 153px; }
  .field.full { width: 320px; }
  .col-a { left: 15px; } .col-b { left: 182px; }
  .volume-label { position: absolute; left: 21px; font-size: 12px; color: var(--ink); }
  .volume-select { position: absolute; left: 184px; width: 72px; height: 32px; background: var(--field); border: 1px solid var(--field-border); border-radius: 2px;
    font-size: 12px; color: var(--field-text); padding-left: 14px; line-height: 30px; }
  .volume-select::after { content: ""; position: absolute; right: 9px; top: 13px; border-left: 6px solid transparent; border-right: 6px solid transparent; border-top: 6px solid #9a9a9a; }
  .submit { position: absolute; left: 15px; top: 294px; width: 319px; height: 42px; background: var(--red); border: 0; border-radius: 3px;
    color: var(--white); font-family: "Oswald", sans-serif; font-weight: 500; font-size: 20px; text-transform: uppercase; }

  .info-band { position: absolute; left: 0; top: 672px; width: 934px; height: 330px; background: var(--blue); color: var(--white); }
  .section-title { font-family: "Oswald", sans-serif; font-weight: 500; font-size: 19px; text-transform: uppercase; }
  .about { position: absolute; left: 129px; top: 38px; width: 392px; }
  .about p { margin-top: 14px; font-size: 13.4px; line-height: 21.6px; }
  .related { position: absolute; left: 571px; top: 38px; width: 230px; }
  .related ul { list-style: none; margin-top: 13px; font-family: "Lato", sans-serif; font-size: 11.5px; line-height: 13px; }
  .related li { position: relative; padding-left: 12px; margin-bottom: 9px; }
  .related li::before { content: ""; position: absolute; left: 1px; top: 4px; width: 5px; height: 5px; border-radius: 50%; background: var(--white); }

  .footer-edge { position: absolute; left: 0; top: 970px; }
  .device-visual { position: absolute; left: 300px; top: 918px; width: 306px; height: 244px;
    background: linear-gradient(160deg, #2b2b2b 0%, #5a5a5a 45%, #d9d9d9 80%, #f2f2f2 100%); border-radius: 10px; }

  .newsletter { position: absolute; left: 118px; top: 998px; }
  .newsletter-title { font-family: "Questrial", sans-serif; font-size: 18px; color: var(--white); text-transform: uppercase; letter-spacing: -0.3px; }
  .newsletter-title b { font-weight: 400; -webkit-text-stroke: 0.6px var(--white); }
  .newsletter-input { position: absolute; left: 0; top: 39px; width: 233px; height: 33px; background: var(--white); border-radius: 17px;
    font-family: "Questrial", sans-serif; font-size: 12px; color: #9a9a9a; padding-left: 14px; line-height: 33px; white-space: nowrap; }
  .subscribe { position: absolute; left: 2px; top: 82px; width: 93px; height: 33px; background: var(--blue); border: 0; border-radius: 17px;
    font-family: "Questrial", sans-serif; font-size: 14px; color: var(--white); }

  .social { position: absolute; left: 611px; top: 1038px; display: flex; gap: 9px; list-style: none; }
  .social li { width: 34px; height: 34px; border-radius: 50%; background: var(--white); }
  .legal { position: absolute; left: 613px; top: 1093px; font-family: "Lato", sans-serif; font-size: 11.5px; color: var(--white); line-height: 16px; }
  .legal nav span { margin: 0 5px; }
</style>
</head>
<body>
  <header class="page-header">
    <h1 class="headline"><span class="lead">Who want to</span><span class="main">Reduce there postage costs</span></h1>
  </header>

  <section class="hero" role="img" aria-label="Photograph of a red wall-mounted post box set into an old stone wall"></section>
  <div class="hero-postbox" role="img" aria-label="Red post box in the stone wall"></div>
  <svg class="hero-edge" width="934" height="60" viewBox="0 0 934 60" aria-hidden="true">
    <polygon points="0,8 160,38 380,8 934,22 934,42 520,16 160,52 0,20" fill="var(--blue)"/>
    <polygon points="0,0 934,0 934,22 380,8 160,38 0,8" fill="var(--red)"/>
  </svg>

  <form class="lead-form">
    <div class="field half col-a" style="top:14px">Name</div>
    <div class="field half col-b" style="top:14px">Business Name</div>
    <div class="field full col-a" style="top:61px">Address</div>
    <div class="field half col-a" style="top:107px">Town</div>
    <div class="field half col-b" style="top:107px">Post Code</div>
    <div class="field half col-a" style="top:154px">Email</div>
    <div class="field half col-b" style="top:154px">Phone</div>
    <span class="volume-label" style="top:209px">Letter Volume Per Week:</span>
    <div class="volume-select" style="top:201px">1</div>
    <span class="volume-label" style="top:256px">Parcel Volume Per Week:</span>
    <div class="volume-select" style="top:248px">1</div>
    <button class="submit" type="button">Submit</button>
  </form>

  <section class="info-band">
    <div class="about">
      <h2 class="section-title">About Us</h2>
      <p>Lorem ipsum dolor sit amet, consectetur adipiscing elit, sed do eiusmod tempor incididunt ut labore et dolore magna aliqua. Ut enim ad minim veniam, quis nostrud exercitation ullamco laboris nisi ut aliquip ex ea commodo consequat. Duis aute irure dolor in reprehenderit in voluptate velit esse cillum dolore eu fugiat nulla pariatur. Excepteur sint occaecat cupidatat non proident, sunt in culpa qui officia deserunt mollit anim id est laborum.</p>
    </div>
    <div class="related">
      <h2 class="section-title">Related Articles</h2>
      <ul>
        <li>Lorem ipsum dolor sit amet, consectetur adipiscing eli</li>
        <li>Lorem ipsum dolor sit amet, consectetur adipiscing eli</li>
        <li>Lorem ipsum dolor sit amet, consectetur adipiscing eli</li>
        <li>Lorem ipsum dolor sit amet, consectetur adipiscing eli</li>
        <li>Lorem ipsum dolor sit amet, consectetur adipiscing eli</li>
      </ul>
    </div>
  </section>

  <svg class="footer-edge" width="934" height="40" viewBox="0 0 934 40" aria-hidden="true">
    <polygon points="0,32 130,5 330,28 934,26 934,40 0,40" fill="var(--red)"/>
  </svg>

  <div class="device-visual" role="img" aria-label="Laptop with envelopes coming out of the screen, symbolising sending mail"></div>

  <div class="newsletter">
    <h2 class="newsletter-title"><b>News</b>letter</h2>
    <div class="newsletter-input">Stay up to date with our latest news</div>
    <button class="subscribe" type="button">Subscribe</button>
  </div>

  <ul class="social" aria-label="Social links">
    <li></li><li></li><li></li><li></li><li></li>
  </ul>
  <div class="legal">
    <p>© 2015 name here. All Rights Reserved</p>
    <nav>Privacy Notice<span>•</span>Legal<span>•</span>Site Map</nav>
  </div>
</body>
</html>
```